Business cards

We need business cards for the logo that you designed for our company. Something simple and clean.

Target Market(s)

Homeowners/ people looking for construction work

Industry/Entity Type

Construction

Contact Information for Business Card

Name: Doug Whitby, Number: 602-555-0174, Email: WhitbyBuildingCompany@mailbox-example.net ROC# 482063

Font styles to use
Serif

Colors

Designer to choose colors to be used in the design.

Requirements
Must have
• On one side of the card I would like to be all of the personal information I have put above along with the company logo that I have attached.
• On the other side of the card I would like the top half of the card to be the logo and then on the bottom half I would like to have the areas of construction we focus on along with an icon that represents it like the picture I have attached.
• Areas we focus on:
• Roofing, Kitchen and bath Remodel, Water Damage, Storm Damage, Fire Damage, Insurance Specialist
• If we could arrange those in alphabetical order.
Nice to have
• I have added 2 company logos a colorful one and a black one it would be nice to see a couple different options the black logo to be more simple and sleek and the colorful logo to be more colorful

```html
<!DOCTYPE html>
<html lang="en">
<head>
<meta charset="utf-8">
<title>Whitby Building Company – Business Cards</title>
<link rel="stylesheet" href="https://fonts.googleapis.com/css2?family=Saira:wght@400;600;700&display=swap">
<style>
  :root {
    --backdrop: #dedede;
    --card-black: #0d0d0d;
    --card-white: #ffffff;
    --ink: #111111;
    --ink-soft: #2a2a2a;
    --accent-blue: #3aa3dc;
    --band-text: #9a9a9a;
    --paper-white: #ffffff;
  }
  * { margin: 0; padding: 0; box-sizing: border-box; }
  html, body {
    width: 1200px;
    height: 1000px;
    overflow: hidden;
    background: var(--backdrop);
    font-family: "Saira", sans-serif;
  }
  .canvas {
    width: 1200px;
    height: 1000px;
    display: flex;
    align-items: center;
    justify-content: center;
    gap: 40px;
  }
  .card {
    position: relative;
    width: 520px;
    height: 297px;
    border-radius: 18px;
    overflow: hidden;
    box-shadow: 0 10px 28px rgba(0,0,0,0.25);
  }
  .brand {
    display: flex;
    align-items: center;
    gap: 12px;
    font-weight: 700;
    text-transform: uppercase;
    letter-spacing: 1.5px;
    line-height: 1;
    white-space: nowrap;
  }
  .brand__mark { flex: none; display: block; }

  /* Back side – black */
  .card--back { background: var(--card-black); color: var(--paper-white); }
  .card--back .brand {
    position: absolute;
    top: 28px;
    left: 0;
    right: 0;
    justify-content: center;
    font-size: 27px;
  }
  .card--back .brand__mark { width: 30px; height: 30px; background: var(--paper-white); }
  .services {
    position: absolute;
    top: 100px;
    left: 20px;
    right: 20px;
    display: grid;
    grid-template-columns: repeat(3, 1fr);
    row-gap: 14px;
    list-style: none;
  }
  .service { text-align: center; }
  .service__pin { display: block; margin: 0 auto 4px; width: 28px; height: 36px; }
  .service__label {
    font-weight: 700;
    font-size: 13px;
    line-height: 1.15;
  }

  /* Front side – white */
  .card--front { background: var(--card-white); color: var(--ink); }
  .card--front .brand {
    position: absolute;
    top: 30px;
    left: 38px;
    font-size: 24px;
  }
  .card--front .brand__mark { width: 26px; height: 26px; background: var(--ink); }
  .front__name {
    position: absolute;
    top: 96px;
    left: 38px;
    font-weight: 700;
    font-size: 21px;
  }
  .front__contact {
    position: absolute;
    top: 140px;
    left: 38px;
    list-style: none;
    font-size: 14px;
    line-height: 1.55;
    color: var(--ink-soft);
  }
  .front__band {
    position: absolute;
    left: 0;
    bottom: 48px;
    width: 200px;
    height: 30px;
    background: var(--ink);
    color: var(--band-text);
    font-size: 13px;
    padding-left: 38px;
    line-height: 30px;
    letter-spacing: 0.5px;
  }
</style>
</head>
<body>
<main class="canvas">

  <section class="card card--back" aria-label="Card back">
    <h1 class="brand"><span class="brand__mark" aria-hidden="true"></span>Whitby Building Company</h1>

    <ul class="services">
      <li class="service">
        <svg class="service__pin" viewBox="0 0 40 52" aria-hidden="true">
          <path d="M20 0C9 0 0 9 0 20c0 14 20 32 20 32s20-18 20-32C40 9 31 0 20 0z" fill="var(--accent-blue)"/>
          <path d="M20 7c2 5 8 8 8 15a8 8 0 0 1-16 0c0-4 2-6 4-8 0 3 1 4 2 5 1-4 0-8 2-12z" fill="var(--paper-white)"/>
        </svg>
        <p class="service__label">Fire<br>Damage</p>
      </li>
      <li class="service">
        <svg class="service__pin" viewBox="0 0 40 52" aria-hidden="true">
          <path d="M20 0C9 0 0 9 0 20c0 14 20 32 20 32s20-18 20-32C40 9 31 0 20 0z" fill="var(--paper-white)"/>
          <rect x="12" y="8" width="16" height="22" rx="1.5" fill="var(--accent-blue)"/>
          <path d="M15 13h10M15 17h10M15 21h10M15 25h7" stroke="var(--paper-white)" stroke-width="1.6"/>
        </svg>
        <p class="service__label">Insurance<br>Specialist</p>
      </li>
      <li class="service">
        <svg class="service__pin" viewBox="0 0 40 52" aria-hidden="true">
          <path d="M20 0C9 0 0 9 0 20c0 14 20 32 20 32s20-18 20-32C40 9 31 0 20 0z" fill="var(--accent-blue)"/>
          <path d="M10 17h20v4a10 10 0 0 1-20 0z" fill="var(--paper-white)"/>
          <path d="M22 17V10h5v3" stroke="var(--paper-white)" stroke-width="2" fill="none"/>
        </svg>
        <p class="service__label">Kitchen and<br>Bath Remodel</p>
      </li>
      <li class="service">
        <svg class="service__pin" viewBox="0 0 40 52" aria-hidden="true">
          <path d="M20 0C9 0 0 9 0 20c0 14 20 32 20 32s20-18 20-32C40 9 31 0 20 0z" fill="var(--paper-white)"/>
          <path d="M20 9l11 10h-4v10h-5v-6h-4v6h-5V19H9z" fill="var(--accent-blue)"/>
        </svg>
        <p class="service__label">Roofing</p>
      </li>
      <li class="service">
        <svg class="service__pin" viewBox="0 0 40 52" aria-hidden="true">
          <path d="M20 0C9 0 0 9 0 20c0 14 20 32 20 32s20-18 20-32C40 9 31 0 20 0z" fill="var(--accent-blue)"/>
          <path d="M13 22a5 5 0 0 1 1-10 7 7 0 0 1 13 2 4 4 0 0 1 0 8z" fill="var(--paper-white)"/>
          <path d="M21 23l-3 5h3l-2 5" stroke="var(--paper-white)" stroke-width="1.8" fill="none"/>
        </svg>
        <p class="service__label">Storm<br>Damage</p>
      </li>
      <li class="service">
        <svg class="service__pin" viewBox="0 0 40 52" aria-hidden="true">
          <path d="M20 0C9 0 0 9 0 20c0 14 20 32 20 32s20-18 20-32C40 9 31 0 20 0z" fill="var(--paper-white)"/>
          <path d="M20 7c4 7 8 11 8 16a8 8 0 0 1-16 0c0-5 4-9 8-16z" fill="var(--accent-blue)"/>
        </svg>
        <p class="service__label">Water<br>Damage</p>
      </li>
    </ul>
  </section>

  <section class="card card--front" aria-label="Card front">
    <h2 class="brand"><span class="brand__mark" aria-hidden="true"></span>Whitby Building Company</h2>
    <p class="front__name">Doug Whitby</p>
    <ul class="front__contact">
      <li>602 555 0174</li>
      <li>WhitbyBuildingCompany@mailbox-example.net</li>
    </ul>
    <p class="front__band">ROC# 482063</p>
  </section>

</main>
</body>
</html>
```